Create a Capability Summary in PowerPoint

CAPABILITY SUMMARY:
We have been asked to provide a Capability Summary by a client and we need your help creating a compelling document!
Our firm specializes in placing cleared technical talent with innovative government contracting firms nationwide. Our goal is to position ourselves as the "go to" talent acquisition company for small and large IT contracting firms in the Federal IT market.
We want you to have creative control over this template, but would like to it include some variation of the following:
Cover Slide w/ Logo
About Us
The Varnuth Difference
Benefits We Offer
-noting that, unlike many recruiting forms, we offer generous PTO, 100%
vesting 401K, and healthcare benefits for all employees
The Talent We Work With
-showcase the fact that we work in the following technical areas:
Network & Systems Engineer, Software Development, Data Science,
and Information Assurance
Clients We Work With
Data-Driven Recruiting Process
-funnel or graphic showcasing our multi-stage recruiting process of :
Sourcing -> Data Discovery -> Automated Outreach -> Candidate
Qualification -> Technical Interview -> Offer & On-boarding
Contact Us
Target Market(s)
IT companies looking for top engineering talent.

```html
<!DOCTYPE html>
<html lang="en">
<head>
<meta charset="utf-8">
<title>Varnuth Capability Summary</title>
<link href="https://fonts.googleapis.com/css2?family=Roboto:wght@400;500;700;900&display=swap" rel="stylesheet">
<style>
:root{
  --navy:#1d4573;
  --navy-deep:#163a63;
  --slate:#3f5787;
  --red:#b8342a;
  --red-soft:#c9473a;
  --grey:#9a9a9a;
  --grey-light:#b9b9b9;
  --ink:#1a1a1a;
  --paper:#ffffff;
  --canvas:#ebebeb;
}
*{box-sizing:border-box;margin:0;padding:0}
html,body{width:1200px;height:1144px;overflow:hidden;background:var(--canvas);font-family:"Roboto",Arial,sans-serif;color:var(--ink)}
.deck{position:relative;width:1200px;height:1144px}
.slide{position:absolute;width:376px;height:211px;background:var(--paper);overflow:hidden;box-shadow:0 2px 6px rgba(0,0,0,.25)}
.c1{left:18px}.c2{left:411px}.c3{left:804px}
.r1{top:13px}.r2{top:239px}.r3{top:465px}.r4{top:690px}.r5{top:916px}
.abs{position:absolute}
.footer-bar{position:absolute;left:0;bottom:0;width:100%;height:7px;background:var(--red)}
.footer-bar::after{content:"";position:absolute;right:8px;top:0;width:32px;height:7px;background:var(--navy);clip-path:polygon(6px 0,100% 0,100% 100%,0 100%)}
.brand-mark{position:absolute;top:6px;right:8px;font-weight:900;font-size:10px;letter-spacing:-.4px;color:var(--navy)}
.slide-title{position:absolute;left:0;width:100%;text-align:center;font-weight:500;font-size:16px;color:var(--ink)}
.fine{font-size:3.7px;line-height:1.45;color:#333;text-align:justify}
.photo{position:absolute}
/* cover */
.cover-photo{inset:0;background:linear-gradient(120deg,#dfe8f4 0%,#b8cbe6 35%,#6f91c4 70%,#3e67a6 100%)}
.cover-logo{left:16px;top:160px;font-size:38px;font-weight:900;letter-spacing:-2px;color:var(--navy)}
/* title slide */
.title-photo{left:0;top:0;width:376px;height:167px;background:radial-gradient(ellipse at 50% 45%,#3f7fc0 0%,#1f4f8e 55%,#0f2f5c 100%)}
.title-main{top:62px;font-size:20px;font-weight:700;color:#fff;letter-spacing:.5px}
.title-sub{top:88px;font-size:12px;color:#fff}
.title-logo{top:170px;font-size:34px;font-weight:900;letter-spacing:-2px;color:var(--navy)}
/* about */
.about-panel{left:18px;top:19px;width:340px;height:170px;background:var(--navy)}
.about-tab{left:0;top:0;width:29px;height:170px;background:var(--navy-deep)}
.about-tab span{position:absolute;left:15px;top:85px;transform:translate(-50%,-50%) rotate(-90deg);color:#fff;font-weight:700;font-size:14px;white-space:nowrap}
.about-photo{left:29px;top:0;width:153px;height:170px;background:linear-gradient(160deg,#5a7fae 0%,#34598a 60%,#24487a 100%)}
.about-logo{left:48px;top:72px;font-size:28px;font-weight:900;letter-spacing:-1.5px;color:#fff}
.about-copy{left:201px;top:12px;width:128px;color:#fff}
.about-copy p{font-size:3.8px;line-height:1.5;text-align:justify;margin-bottom:5px}
/* difference grid */
.diff-title{left:14px;top:82px;width:130px;text-align:center;font-size:16.5px;font-weight:500;line-height:1.3}
.diff-item{position:absolute;width:88px}
.diff-item .rule{width:25px;height:2px;background:var(--navy)}
.diff-item .rule.red{background:var(--red)}
.diff-item .num{font-size:12px;font-weight:700;margin-top:1px}
.diff-item .label{font-size:5.5px;font-weight:700;margin:2px 0}
/* difference lists */
.diff-accent{left:0;top:38px;width:18px;height:134px;background:var(--red)}
.diff-heading{left:29px;top:36px;font-size:16px;font-weight:500;line-height:1.4}
.diff-para{left:29px;top:120px;width:122px}
.list-head{position:absolute;left:168px;width:187px;height:8px;background:var(--navy);color:#fff;font-size:4.5px;padding:1.6px 3px;font-weight:500}
.bullets{position:absolute;left:172px;width:180px;list-style:none}
.bullets li{font-size:3.6px;color:#444;line-height:1.75}
.bullets li::before{content:"•";margin-right:3px}
/* benefits pills */
.ben-title{top:28px;font-size:17px}
.ben-sub{top:52px;font-size:6.5px;font-weight:700;line-height:1.3}
.pill{position:absolute;height:30px;background:var(--navy);color:#fff;display:flex;align-items:center;justify-content:center}
.pill-pto{left:115px;top:83px;width:139px;border-radius:15px;clip-path:polygon(0 0,80% 0,100% 100%,0 100%);font-size:13px;font-weight:500}
.pill-401k{left:116px;top:122px;width:139px;border-radius:15px;clip-path:polygon(0 0,100% 0,100% 100%,8% 100%);font-size:8.5px}
.pill .dot{position:absolute;top:4px;width:22px;height:22px;border-radius:50%;background:var(--red)}
.ben-note{top:175px;font-size:8.5px}
/* benefits band */
.band-photo{inset:0;background:linear-gradient(180deg,#4c5f76 0%,#3a5474 50%,#24497a 52%,#1f4676 100%)}
.band-box{left:0;top:0;width:190px;height:106px;background:var(--paper)}
.band-title{left:16px;top:44px;font-size:17px;font-weight:500}
.band-note{left:205px;top:22px;width:160px;text-align:center;color:#e8edf4;font-size:7.4px;line-height:1.55}
.tab{position:absolute;top:92px;width:23px;height:32px;background:var(--red);border-radius:3px 3px 0 0;color:#fff;font-size:7.5px;font-weight:700;text-align:center;padding-top:17px}
.tab::before{content:"";position:absolute;left:6px;top:11px;width:11px;height:1px;background:rgba(255,255,255,.7)}
.tab-copy{position:absolute;top:133px;width:68px;color:#dbe3ee;font-size:6.3px;line-height:1.8}
/* talent */
.talent-title{top:12px;font-size:15.5px;font-weight:700}
.talent-sub{top:30px;font-size:10px;font-weight:500}
.area{position:absolute;font-size:7.8px;font-weight:700;line-height:1.4}
.area.navy{color:var(--navy)}.area.red{color:var(--red)}
.area.right-al{text-align:right}
/* clients */
.clients-band{left:0;top:0;width:376px;height:211px}
.clients-title{left:40px;top:76px;width:104px;text-align:center;color:#fff;font-size:16px;font-weight:700;line-height:1.3}
.client{position:absolute;width:57px;height:27px;background:#fff;box-shadow:0 1px 3px rgba(0,0,0,.25);display:flex;align-items:center;justify-content:center;font-size:8.5px;font-weight:700;text-align:center;line-height:1.05}
.client.navy{color:var(--navy)}.client.red{color:var(--red)}.client.ink{color:var(--ink)}
/* process */
.process-title{left:19px;top:72px;font-size:16px;font-weight:700;line-height:1.3}
/* contact */
.contact-title{top:20px;font-size:17px;font-weight:500}
.contact-band{left:0;top:52px;width:376px;height:142px;background:linear-gradient(135deg,#3e5f8c 0%,#2c5180 50%,#35598a 100%)}
.contact-logo{left:30px;top:106px;font-size:30px;font-weight:900;letter-spacing:-2px;color:#fff}
.contact-row{position:absolute;left:202px;width:165px;display:flex;align-items:center;gap:6px;color:#fff;font-size:6px;line-height:1.4;padding-bottom:3px;border-bottom:.6px solid rgba(255,255,255,.55)}
.contact-row.last{border-bottom:none}
.contact-row svg{flex:none}
/* checklist */
.check-box{left:17px;top:77px;width:170px}
.check-head{background:var(--navy);color:#fff;font-size:3.6px;padding:3px 5px;line-height:1.4;text-align:center}
.check-row{display:flex;align-items:center;gap:5px;border:1px solid var(--navy);margin-top:3px;padding:3px 4px}
.check-row p{font-size:3.5px;line-height:1.45;color:#333}
.side-copy{left:200px;top:74px;width:160px}
.side-copy p{margin-bottom:6px}
/* pie */
.pie-sub{top:45px;font-size:3.8px;color:#333}
.pie-points{left:20px;top:68px;width:164px}
.pie-points h4{font-size:5.5px;font-weight:500;margin-top:5px}
.pie-points h4::before{content:"▸ ";color:var(--navy)}
.pie-points p{font-size:3.4px;line-height:1.4;color:#333}
/* columns */
.cols-photo{left:0;top:103px;width:376px;height:108px;background:radial-gradient(ellipse at 40% 60%,#4b79ad 0%,#2d578c 55%,#1e4575 100%)}
.col{position:absolute;top:48px;width:74px;text-align:center}
.col h5{font-size:4.8px;font-weight:700;margin-bottom:3px}
.col p{font-size:3.5px;line-height:1.45;color:#333}
.col.feature{top:45px;width:84px;height:80px;background:var(--navy);padding:4px 6px}
.col.feature h5,.col.feature p{color:#fff}
/* keyboard */
.kb-band{left:30px;top:93px;width:313px;height:54px;background:var(--navy)}
.kb-photo{left:68px;top:54px;width:248px;height:81px;background:linear-gradient(160deg,#f1f3f5 0%,#d7dde3 50%,#5fb6dc 62%,#3aa2d2 80%,#e6e9ec 100%)}
.kb-copy{position:absolute;top:159px;width:150px}
</style>
</head>
<body>
<main class="deck">

  <!-- Cover -->
  <section class="slide c1 r1">
    <div class="photo cover-photo" role="img" aria-label="Photo of a humanoid robot touching a holographic data screen"></div>
    <div class="abs cover-logo">VARNUTH</div>
  </section>

  <!-- Title -->
  <section class="slide c2 r1">
    <div class="photo title-photo" role="img" aria-label="Photo of a finger touching a glowing network of connected people icons"></div>
    <div class="slide-title title-main">PRESENTATION TITLE</div>
    <div class="slide-title title-sub">Sub title goes here</div>
    <div class="slide-title title-logo">VARNUTH</div>
  </section>

  <!-- About us -->
  <section class="slide c3 r1">
    <div class="brand-mark">VARNUTH</div>
    <div class="abs about-panel">
      <div class="abs about-tab"><span>ABOUT US</span></div>
      <div class="photo about-photo" role="img" aria-label="Blue-toned photo of a robot with data graphics"></div>
      <div class="abs about-logo">VARNUTH</div>
      <div class="abs about-copy">
        <p>We place cleared technical talent with innovative government contracting firms nationwide. Our team pairs deep federal IT insight with a rigorous, data-led search so every hire fits the mission, the clearance level and the culture of the team they join. Clients count on us for speed and quality.</p>
        <p>From small primes to large integrators, we are the go-to talent partner in the Federal IT market. We source, vet and present engineers who are ready to contribute from day one, and we stay close after placement to make sure each match lasts and grows.</p>
      </div>
    </div>
    <div class="footer-bar"></div>
  </section>

  <!-- Difference grid -->
  <section class="slide c1 r2">
    <div class="brand-mark">VARNUTH</div>
    <div class="abs diff-title">The Varnuth Difference</div>
    <div class="diff-item" style="left:155px;top:20px">
      <div class="rule"></div><div class="num">01</div><div class="label">Your Text Here</div>
      <p class="fine">Cleared engineers ready to work on day one, screened for skill, fit and clearance, so your team can bid and deliver with full confidence every time.</p>
    </div>
    <div class="diff-item" style="left:261px;top:20px">
      <div class="rule red"></div><div class="num">02</div><div class="label">Your Text Here</div>
      <p class="fine">A data-driven search that finds passive talent fast, tracks every step and keeps you informed with clear reports from first call to final offer.</p>
    </div>
    <div class="diff-item" style="left:155px;top:113px">
      <div class="rule red"></div><div class="num">03</div><div class="label">Your Text Here</div>
      <p class="fine">Deep roots in the Federal IT market mean we know the roles, the contracts and the people, and we speak the language of your program managers.</p>
    </div>
    <div class="diff-item" style="left:261px;top:113px">
      <div class="rule"></div><div class="num">04</div><div class="label">Your Text Here</div>
      <p class="fine">Strong employee benefits help us attract and keep top engineers, which gives you stable teams, lower turnover and steady performance on contract.</p>
    </div>
    <div class="footer-bar"></div>
  </section>

  <!-- Difference lists -->
  <section class="slide c2 r2">
    <div class="brand-mark">VARNUTH</div>
    <div class="abs diff-accent"></div>
    <div class="abs diff-heading">The<br>Varnuth<br>Difference</div>
    <p class="abs fine diff-para">We focus on one market and do it well. Our recruiters know cleared IT roles inside out, and our process turns data into fast, accurate matches for firms that need proven engineers now.</p>
    <div class="list-head" style="top:51px">Why firms choose us</div>
    <ul class="bullets" style="top:62px">
      <li>Cleared talent across every major federal IT role</li>
      <li>Fast shortlists backed by real market data</li>
      <li>Technical screening led by working engineers</li>
      <li>Clear updates at every stage of each search</li>
      <li>Support that continues well after placement</li>
    </ul>
    <div class="list-head" style="top:122px">What candidates get</div>
    <ul class="bullets" style="top:133px">
      <li>Generous paid time off from the first day</li>
      <li>A 401K plan with full and immediate vesting</li>
      <li>Healthcare benefits for every employee</li>
      <li>Roles matched to skills and career goals</li>
      <li>A recruiter who stays in touch over time</li>
    </ul>
    <div class="footer-bar"></div>
  </section>

  <!-- Benefits pills -->
  <section class="slide c3 r2">
    <div class="brand-mark">VARNUTH</div>
    <div class="slide-title ben-title">Benefits We Offer</div>
    <div class="slide-title ben-sub">noting that, unlike many recruiting forms,<br>we offer generous</div>
    <div class="pill pill-pto"><span class="dot" style="left:4px"></span>PTO</div>
    <div class="pill pill-401k"><span class="dot" style="right:4px"></span>100% vesting 401K</div>
    <div class="slide-title ben-note">and healthcare benefits for all employees</div>
    <div class="footer-bar"></div>
  </section>

  <!-- Benefits band -->
  <section class="slide c1 r3">
    <div class="photo band-photo" role="img" aria-label="Dimmed photo of a modern glass building interior in blue tones"></div>
    <div class="abs band-box"></div>
    <div class="abs band-title">Benefits We Offer</div>
    <p class="abs band-note">Noting that, unlike many recruiting forms, we offer generous PTO, 100% vesting 401K, and healthcare benefits for all employees.</p>
    <div class="tab" style="left:17px">01</div>
    <div class="tab" style="left:88px">02</div>
    <div class="tab" style="left:159px">03</div>
    <div class="tab" style="left:230px">04</div>
    <div class="tab" style="left:301px">05</div>
    <p class="tab-copy" style="left:17px">Generous paid time off for every new hire.</p>
    <p class="tab-copy" style="left:88px">A 401K plan with full vesting from day one.</p>
    <p class="tab-copy" style="left:159px">Healthcare cover for all our employees.</p>
    <p class="tab-copy" style="left:230px">Training budget for new certifications.</p>
    <p class="tab-copy" style="left:301px">Career paths shaped with each engineer.</p>
  </section>

  <!-- Talent -->
  <section class="slide c2 r3">
    <div class="brand-mark">VARNUTH</div>
    <div class="slide-title talent-title">The Talent We Work With</div>
    <div class="slide-title talent-sub">Technical areas:</div>
    <svg class="abs" style="left:0;top:0" width="376" height="211" viewBox="0 0 376 211" aria-hidden="true">
      <g fill="none" stroke-width="6">
        <circle cx="150" cy="92" r="33" stroke="var(--navy)"/>
        <circle cx="215" cy="92" r="33" stroke="var(--red)"/>
        <circle cx="150" cy="156" r="33" stroke="var(--red)"/>
        <circle cx="215" cy="156" r="33" stroke="var(--slate)"/>
      </g>
      <g fill="#fff">
        <circle cx="150" cy="92" r="25"/><circle cx="215" cy="92" r="25"/>
        <circle cx="150" cy="156" r="25"/><circle cx="215" cy="156" r="25"/>
      </g>
      <g fill="none" stroke="var(--ink)" stroke-width="1.4">
        <rect x="141" y="86" width="10" height="13"/><circle cx="157" cy="90" r="6"/>
        <circle cx="215" cy="92" r="10"/><ellipse cx="215" cy="92" rx="4.5" ry="10"/>
        <line x1="205" y1="92" x2="225" y2="92"/><line x1="207" y1="86" x2="223" y2="86"/><line x1="207" y1="98" x2="223" y2="98"/>
        <rect x="140" y="147" width="20" height="13"/><line x1="136" y1="163" x2="164" y2="163"/>
        <rect x="205" y="147" width="20" height="13"/><line x1="201" y1="163" x2="229" y2="163"/>
        <rect x="211" y="152" width="8" height="6"/><path d="M212.5 152v-2a2.5 2.5 0 0 1 5 0v2"/>
      </g>
      <g fill="var(--navy)"><circle cx="101" cy="86" r="1.4"/><circle cx="261" cy="152" r="1.4"/></g>
      <g fill="var(--red)"><circle cx="265" cy="86" r="1.4"/><circle cx="101" cy="152" r="1.4"/></g>
    </svg>
    <div class="area navy right-al" style="right:279px;top:80px">Network &amp; Systems<br>Engineer</div>
    <div class="area red" style="left:273px;top:81px">Data Science</div>
    <div class="area red right-al" style="right:279px;top:146px">Software<br>Development</div>
    <div class="area navy" style="left:270px;top:147px">Information<br>Assurance</div>
    <div class="footer-bar"></div>
  </section>

  <!-- Clients -->
  <section class="slide c3 r3">
    <div class="brand-mark">VARNUTH</div>
    <svg class="abs clients-band" viewBox="0 0 376 211" aria-hidden="true"><polygon points="47,0 165,0 144,211 19,211" fill="var(--navy)"/></svg>
    <div class="abs clients-title">Clients<br>We Work<br>With</div>
    <div class="client ink" style="left:190px;top:45px">Name or<br>LOGO</div>
    <div class="client red" style="left:259px;top:45px">Brightwell</div>
    <div class="client navy" style="left:190px;top:79px">Orlo</div>
    <div class="client navy" style="left:259px;top:79px">Tessaly</div>
    <div class="client ink" style="left:190px;top:113px">Quintera</div>
    <div class="client red" style="left:259px;top:113px">Ravenmoor</div>
    <div class="client ink" style="left:190px;top:147px">Solvane</div>
    <div class="client red" style="left:259px;top:147px">Kairo</div>
    <div class="footer-bar"></div>
  </section>

  <!-- Process -->
  <section class="slide c1 r4">
    <div class="brand-mark">VARNUTH</div>
    <div class="abs process-title">Data-Driven<br>Recruiting<br>Process</div>
    <svg class="abs" style="left:0;top:0" width="376" height="211" viewBox="0 0 376 211" aria-hidden="true">
      <path d="M140 97l9 9-9 9M151 97l9 9-9 9" fill="none" stroke="var(--navy)" stroke-width="5"/>
      <g fill="none" stroke-width="42" stroke-dasharray="64 338">
        <circle cx="254" cy="104" r="64" stroke="var(--red)" transform="rotate(-140 254 104)"/>
        <circle cx="254" cy="104" r="64" stroke="var(--red-soft)" transform="rotate(-80 254 104)"/>
        <circle cx="254" cy="104" r="64" stroke="var(--navy)" transform="rotate(-20 254 104)"/>
        <circle cx="254" cy="104" r="64" stroke="var(--navy)" transform="rotate(40 254 104)"/>
        <circle cx="254" cy="104" r="64" stroke="var(--grey)" transform="rotate(100 254 104)"/>
        <circle cx="254" cy="104" r="64" stroke="var(--grey-light)" transform="rotate(160 254 104)"/>
      </g>
      <g fill="#fff" font-family="Roboto, Arial, sans-serif" font-size="6" text-anchor="middle">
        <text x="232" y="42">Offer &amp; On-</text><text x="232" y="49">boarding</text>
        <text x="295" y="58">Sourcing</text>
        <text x="317" y="113">Data</text><text x="320" y="120">Discovery</text>
        <text x="278" y="162">Automated</text><text x="278" y="169">Outreach</text>
        <text x="214" y="151">Candidate</text><text x="214" y="158">Qualification</text>
        <text x="192" y="91">Technical</text><text x="192" y="98">Interview</text>
      </g>
      <text x="254" y="108" text-anchor="middle" font-family="Roboto, Arial, sans-serif" font-weight="900" font-size="13" letter-spacing="-.5" fill="var(--navy)">VARNUTH</text>
    </svg>
    <div class="footer-bar"></div>
  </section>

  <!-- Contact -->
  <section class="slide c2 r4">
    <div class="brand-mark">VARNUTH</div>
    <div class="slide-title contact-title">Contact Us</div>
    <div class="photo contact-band" role="img" aria-label="Blue-tinted photo of a glass roof structure"></div>
    <div class="abs contact-logo">VARNUTH</div>
    <div class="contact-row" style="top:68px">
      <svg width="14" height="14" viewBox="0 0 14 14"><circle cx="7" cy="7" r="7" fill="#5d7aa3"/><path d="M4.5 3.8l1.5-.3.8 1.8-.9.7a5 5 0 0 0 2.1 2.1l.7-.9 1.8.8-.3 1.5c-3.3 0-6-2.7-6-5.7z" fill="#fff"/></svg>
      <span>555-014-2298</span></div>
    <div class="contact-row" style="top:97px">
      <svg width="14" height="14" viewBox="0 0 14 14"><circle cx="7" cy="7" r="7" fill="#5d7aa3"/><rect x="4" y="5" width="6" height="4.5" fill="#fff"/><path d="M4 5l3 2.3L10 5" fill="none" stroke="#5d7aa3" stroke-width=".6"/></svg>
      <span>info@varnuth-us.com</span></div>
    <div class="contact-row" style="top:126px">
      <svg width="14" height="14" viewBox="0 0 14 14"><circle cx="7" cy="7" r="7" fill="#5d7aa3"/><g fill="none" stroke="#fff" stroke-width=".7"><circle cx="7" cy="7" r="3.5"/><ellipse cx="7" cy="7" rx="1.5" ry="3.5"/><line x1="3.5" y1="7" x2="10.5" y2="7"/></g></svg>
      <span>http://varnuth-us.com/</span></div>
    <div class="contact-row last" style="top:155px">
      <svg width="14" height="14" viewBox="0 0 14 14"><circle cx="7" cy="7" r="7" fill="#5d7aa3"/><path d="M7 11s-3-3.2-3-5a3 3 0 0 1 6 0c0 1.8-3 5-3 5z" fill="#fff"/><circle cx="7" cy="6" r="1" fill="#5d7aa3"/></svg>
      <span>47 Alder Crest Way<br>Fairhaven, VA 20110</span></div>
    <div class="footer-bar"></div>
  </section>

  <!-- Checklist -->
  <section class="slide c3 r4">
    <div class="brand-mark">VARNUTH</div>
    <div class="slide-title" style="top:26px;font-size:15px">Lorem ipsum dolor sit amet</div>
    <div class="abs check-box">
      <div class="check-head">Every search follows clear steps so clients always know where each open role stands.</div>
      <div class="check-row"><svg width="10" height="10" viewBox="0 0 10 10"><circle cx="5" cy="5" r="4.4" fill="none" stroke="var(--navy)" stroke-width=".9"/><path d="M3 5l1.5 1.5L7 3.8" fill="none" stroke="var(--navy)" stroke-width="1"/></svg><p>We map the role, the clearance and the team before the search begins for real.</p></div>
      <div class="check-row"><svg width="10" height="10" viewBox="0 0 10 10"><circle cx="5" cy="5" r="4.4" fill="none" stroke="var(--navy)" stroke-width=".9"/><path d="M3 5l1.5 1.5L7 3.8" fill="none" stroke="var(--navy)" stroke-width="1"/></svg><p>Market data shows where the best cleared engineers are and what they expect.</p></div>
      <div class="check-row"><svg width="10" height="10" viewBox="0 0 10 10"><circle cx="5" cy="5" r="4.4" fill="none" stroke="var(--navy)" stroke-width=".9"/><path d="M3 5l1.5 1.5L7 3.8" fill="none" stroke="var(--navy)" stroke-width="1"/></svg><p>Engineers on our team run the technical screen before any profile is sent.</p></div>
      <div class="check-row"><svg width="10" height="10" viewBox="0 0 10 10"><circle cx="5" cy="5" r="4.4" fill="none" stroke="var(--navy)" stroke-width=".9"/><path d="M3 5l1.5 1.5L7 3.8" fill="none" stroke="var(--navy)" stroke-width="1"/></svg><p>We guide offer and onboarding so new hires start fast and stay for the long run.</p></div>
    </div>
    <div class="abs side-copy fine">
      <p>Federal IT programs move fast and need people who can hold a clearance and deliver results. We build pipelines of vetted engineers before roles open, so our clients can staff new contracts quickly and with confidence in every hire.</p>
      <p>Our recruiters track response rates, time to fill and retention for each search. These numbers guide where we look and how we reach out, which keeps quality high and delays low.</p>
      <p>After each placement we check in with both sides, learn what worked and feed it back into the next search for the same client.</p>
    </div>
    <div class="footer-bar"></div>
  </section>

  <!-- Pie -->
  <section class="slide c1 r5">
    <div class="brand-mark">VARNUTH</div>
    <div class="slide-title" style="top:26px;font-size:15.5px">Lorem ipsum dolor sit amet</div>
    <div class="slide-title pie-sub">Share of placements by technical area across our recent<br>federal IT searches for prime and sub contractors.</div>
    <div class="abs pie-points">
      <h4>Lorem ipsum dolor</h4><p>Network and systems roles lead demand, driven by large cloud and data center moves across many agencies this year.</p>
      <h4>Lorem ipsum dolor</h4><p>Software development follows, with strong need for cleared full stack and DevSecOps engineers on new contracts.</p>
      <h4>Lorem ipsum dolor</h4><p>Data science roles grow each quarter as agencies invest in analytics, automation and modern data platforms.</p>
      <h4>Lorem ipsum dolor</h4><p>Information assurance stays steady, as every program needs cleared security staff to keep systems compliant.</p>
    </div>
    <svg class="abs" style="left:0;top:0" width="376" height="211" viewBox="0 0 376 211" aria-hidden="true">
      <g fill="none" stroke-width="48">
        <circle cx="275" cy="118" r="24" stroke="var(--navy)" stroke-dasharray="87.5 63.3" transform="rotate(120 275 118)"/>
        <circle cx="275" cy="118" r="24" stroke="var(--red-soft)" stroke-dasharray="34.7 116.1" transform="rotate(-31 275 118)"/>
        <circle cx="275" cy="118" r="24" stroke="var(--red)" stroke-dasharray="15.1 135.7" transform="rotate(52 275 118)"/>
        <circle cx="275" cy="118" r="24" stroke="var(--slate)" stroke-dasharray="13.6 137.2" transform="rotate(88 275 118)"/>
      </g>
      <g fill="#fff" font-family="Roboto, Arial, sans-serif" font-size="6.5" text-anchor="middle">
        <text x="248" y="106">58%</text><text x="301" y="117">23%</text>
        <text x="288" y="153">10%</text><text x="265" y="156">9%</text>
      </g>
    </svg>
    <div class="footer-bar"></div>
  </section>

  <!-- Columns -->
  <section class="slide c2 r5">
    <div class="brand-mark">VARNUTH</div>
    <div class="slide-title" style="top:15px;font-size:15.5px">Lorem ipsum dolor sit amet</div>
    <div class="photo cols-photo" role="img" aria-label="Photo of a hand touching a network of connected people icons"></div>
    <div class="col" style="left:15px"><h5>Your Contents Here</h5><p>Short intake call to define the role, the clearance and the timeline for hire.</p></div>
    <div class="col" style="left:97px"><h5>Your Contents Here</h5><p>Targeted sourcing from our cleared talent pool and trusted referral network.</p></div>
    <div class="col feature" style="left:179px"><h5>Your Contents Here</h5><p>Every candidate is screened by an engineer, checked for clearance and matched to team culture before you see a single profile from us.</p></div>
    <div class="col" style="left:277px"><h5>Your Contents Here</h5><p>Offer support and onboarding so new hires start on time and stay engaged.</p></div>
    <div class="footer-bar"></div>
  </section>

  <!-- Keyboard -->
  <section class="slide c3 r5">
    <div class="brand-mark">VARNUTH</div>
    <div class="slide-title" style="top:28px;font-size:15.5px">Lorem ipsum dolor sit amet</div>
    <div class="abs kb-band"></div>
    <div class="photo kb-photo" role="img" aria-label="Close-up photo of a keyboard with a blue recruitment key"></div>
    <p class="fine kb-copy" style="left:30px">We help IT firms find top engineering talent for federal work. Our focus on cleared roles and our data-led process mean faster hires, better fits and teams that stay together through the life of each contract.</p>
    <p class="fine kb-copy" style="left:197px">Small and large contractors alike rely on us when deadlines are tight. Tell us the role and we will deliver a short list of proven, cleared engineers ready to interview within days.</p>
    <div class="footer-bar"></div>
  </section>

</main>
</body>
</html>
```